Card Design for my dog training business Rustpaw Obedience

Need a business card design for my dog training business with my new logo. Want the card to come off professional yet fun. Want it to be very eye catchy as well. I normally have these at vet clinics, pet stores, and groomers. so need it to look better than my competitors.
Target Market(s)
dog owners
Industry/Entity Type
Dog Training
Contact Information for Business Card
needs logo, my name and info
Font styles to use
Serif
Colors
0255a3
ffffff
ec1f27
000000
333333
fbfbfb
Requirements
Must have
- Rustpaw Obedience
- Hollis Brandt
- 415 903 2267
- info@rustpawobedience.example
- www.rustpawobedience.example

```html
<!DOCTYPE html>
<html lang="en">
<head>
<meta charset="utf-8">
<title>Rustpaw Obedience – Business Card</title>
<link href="https://fonts.googleapis.com/css2?family=EB+Garamond:ital,wght@0,400;1,400&family=Open+Sans:wght@400&display=swap" rel="stylesheet">
<style>
  :root {
    --backdrop: #e8e8ea;
    --card: #ffffff;
    --ink: #333333;
    --ink-dark: #000000;
    --rule: #333333;
  }
  * { margin: 0; padding: 0; box-sizing: border-box; }
  html, body {
    width: 1200px; height: 1200px; overflow: hidden;
    background: var(--backdrop);
  }
  .canvas { position: relative; width: 1200px; height: 1200px; }

  .card {
    position: absolute;
    background: var(--card);
    color: var(--ink);
  }
  .card--front { left: 196px; top: 56px; width: 808px; height: 486px; }
  .card--back  { left: 214px; top: 634px; width: 790px; height: 484px; }

  .brand-name {
    position: absolute;
    font-family: "EB Garamond", serif;
    font-weight: 400;
    color: var(--ink);
    text-align: center;
    line-height: 1.05;
  }
  .card--front .brand-name {
    left: 0; right: 0; top: 196px;
    font-size: 60px;
  }
  .card--back .brand-name {
    left: 40px; width: 250px; top: 150px;
    font-size: 40px;
  }

  .star { position: absolute; fill: var(--ink); }
  .star--left  { left: 60px; top: 240px; }
  .star--right { left: 724px; top: 240px; }
  .star-row { position: absolute; left: 123px; top: 355px; }

  .tagline {
    position: absolute; left: 0; right: 0; top: 408px;
    text-align: center;
    font-family: "EB Garamond", serif;
    font-style: italic;
    font-size: 30px;
    color: var(--ink);
  }

  .divider {
    position: absolute; left: 330px; top: 118px;
    width: 1px; height: 251px; background: var(--rule);
  }

  .person-name {
    position: absolute; left: 374px; top: 130px;
    font-family: "EB Garamond", serif;
    font-size: 44px; font-weight: 400;
    color: var(--ink);
  }
  .person-rule {
    position: absolute; left: 376px; top: 189px;
    width: 113px; height: 2px; background: var(--rule);
  }

  .contact-list { position: absolute; left: 373px; top: 241px; list-style: none; }
  .contact-item {
    display: flex; align-items: center; gap: 10px;
    height: 37px;
    font-family: "Open Sans", sans-serif;
    font-size: 20px; color: var(--ink-dark);
  }
  .contact-icon { width: 22px; height: 22px; flex: none; }
</style>
</head>
<body>
<main class="canvas">

  <section class="card card--front" aria-label="Card front">
    <div class="brand-name">Rustpaw Obedience</div>
    <svg class="star star--left" width="24" height="24" viewBox="0 0 24 24" aria-hidden="true"><polygon points="12,1 15,9 23,9 16.5,14 19,22 12,17 5,22 7.5,14 1,9 9,9"/></svg>
    <svg class="star star--right" width="24" height="24" viewBox="0 0 24 24" aria-hidden="true"><polygon points="12,1 15,9 23,9 16.5,14 19,22 12,17 5,22 7.5,14 1,9 9,9"/></svg>
    <p class="tagline">“Good manners for every dog, one lesson at a time.”</p>
  </section>

  <section class="card card--back" aria-label="Card back">
    <div class="brand-name">Rustpaw<br>Obedience</div>
    <svg class="star-row" width="86" height="24" viewBox="0 0 86 24" aria-hidden="true" fill="#333333">
      <polygon points="9,5 11,10 16,10 12,13 13.5,18 9,15 4.5,18 6,13 2,10 7,10"/>
      <polygon points="43,1 46,9 54,9 47.5,14 50,22 43,17 36,22 38.5,14 32,9 40,9"/>
      <polygon points="77,5 79,10 84,10 80,13 81.5,18 77,15 72.5,18 74,13 70,10 75,10"/>
    </svg>
    <div class="divider"></div>

    <h1 class="person-name">Hollis Brandt</h1>
    <div class="person-rule"></div>

    <ul class="contact-list">
      <li class="contact-item">
        <svg class="contact-icon" viewBox="0 0 22 22" aria-hidden="true">
          <circle cx="11" cy="11" r="11" fill="#333333"/>
          <path d="M7.5 5.5l2 2-1.2 1.5a7 7 0 0 0 4.7 4.7l1.5-1.2 2 2-1.5 1.8c-4.5-.3-8.8-4.6-9.1-9.1z" fill="#ffffff"/>
        </svg>
        <span>415 903 2267</span>
      </li>
      <li class="contact-item">
        <svg class="contact-icon" viewBox="0 0 22 22" aria-hidden="true">
          <circle cx="11" cy="11" r="11" fill="#333333"/>
          <rect x="5.5" y="7" width="11" height="8" fill="none" stroke="#ffffff" stroke-width="1.3"/>
          <path d="M5.5 7l5.5 4.5L16.5 7" fill="none" stroke="#ffffff" stroke-width="1.3"/>
        </svg>
        <span>info@rustpawobedience.example</span>
      </li>
      <li class="contact-item">
        <svg class="contact-icon" viewBox="0 0 22 22" aria-hidden="true">
          <circle cx="11" cy="11" r="11" fill="#333333"/>
          <g fill="none" stroke="#ffffff" stroke-width="1.1">
            <circle cx="11" cy="11" r="6"/>
            <ellipse cx="11" cy="11" rx="2.6" ry="6"/>
            <path d="M5 11h12M6 8h10M6 14h10"/>
          </g>
        </svg>
        <span>www.rustpawobedience.example</span>
      </li>
    </ul>
  </section>

</main>
</body>
</html>
```